Visitenkarte erstellen für Reiki Praxis

Visitenkarten für Reiki Praxis Doppelseitig

business cards reiki practice double-sided

The background can also be a different color

```html
<!DOCTYPE html>
<html lang="en">
<head>
<meta charset="utf-8">
<title>Stillwater Reiki – Business Cards</title>
<link rel="stylesheet" href="https://fonts.googleapis.com/css2?family=Montserrat:wght@300;400&display=swap">
<style>
  :root {
    --stage: #2b2b2b;
    --card-black: #050507;
    --card-white: #f7f7f7;
    --ink-dark: #1a1a1a;
    --ink-light: #f2f2f2;
    --gold: #d9a432;
    --rose: #c9768f;
    --mark-grey: #bdb6bc;
  }
  * { margin: 0; padding: 0; box-sizing: border-box; }
  html, body {
    width: 1200px; height: 732px; overflow: hidden;
    background: var(--stage);
    font-family: "Montserrat", sans-serif;
  }
  .canvas { position: relative; width: 1200px; height: 732px; }

  .card {
    position: absolute; top: 242px;
    width: 436px; height: 248px;
    background: var(--card-black);
    overflow: hidden;
    box-shadow: 0 8px 18px rgba(0,0,0,0.45);
  }
  .card--front { left: 144px; }
  .card--back  { left: 621px; }

  /* front: white brand strip */
  .brand-strip {
    position: absolute; left: 0; top: 0;
    width: 143px; height: 248px;
    background: var(--card-white);
  }
  .brand-strip__name {
    position: absolute; left: 82px; top: 25px;
    height: 199px;
    writing-mode: vertical-rl; transform: rotate(180deg);
    font-size: 18px; font-weight: 400; letter-spacing: 0.5px;
    color: var(--ink-dark); text-align: center; white-space: nowrap;
  }
  .brand-strip__dot {
    position: absolute; left: 44px; top: 118px;
    width: 14px; height: 14px; border-radius: 50%;
    background: var(--ink-dark);
  }

  .divider {
    position: absolute; left: 157px; top: 25px;
    width: 1px; height: 198px;
    background: linear-gradient(var(--gold), var(--rose));
  }

  .contact {
    position: absolute; left: 189px; top: 24px;
    color: var(--ink-light);
  }
  .contact__name { font-size: 15.5px; font-weight: 400; letter-spacing: 0.3px; line-height: 1.1; }
  .contact__role { font-size: 11.5px; font-weight: 400; margin-top: 1px; }
  .contact__address {
    position: absolute; top: 106px; left: 0;
    font-size: 11.5px; line-height: 15px; white-space: nowrap;
  }
  .contact__lines {
    position: absolute; top: 161px; left: 0;
    list-style: none; font-size: 11.5px; line-height: 15px; white-space: nowrap;
  }
  .contact__lines li { display: flex; align-items: center; gap: 7px; }
  .contact__lines svg { width: 11px; height: 11px; flex: none; }

  /* back */
  .back-mark {
    position: absolute; left: 0; right: 0; top: 136px;
    text-align: center;
    font-size: 19.5px; font-weight: 300; letter-spacing: 1.5px;
    color: var(--mark-grey);
  }
</style>
</head>
<body>
<main class="canvas">

  <section class="card card--front" aria-label="Business card front">
    <div class="brand-strip">
      <span class="brand-strip__dot"></span>
      <span class="brand-strip__name">STILLWATER REIKI</span>
    </div>
    <span class="divider"></span>
    <div class="contact">
      <p class="contact__name">ELENA BRIGHTWATER</p>
      <p class="contact__role">Owner</p>
      <p class="contact__address">00 NE Harbor Lane<br>Palmview, FL 00000</p>
      <ul class="contact__lines">
        <li>
          <svg viewBox="0 0 24 24" aria-hidden="true"><path fill="var(--gold)" d="M6.6 10.8a15.1 15.1 0 0 0 6.6 6.6l2.2-2.2a1 1 0 0 1 1-.25 11.4 11.4 0 0 0 3.6.57 1 1 0 0 1 1 1V20a1 1 0 0 1-1 1A17 17 0 0 1 3 4a1 1 0 0 1 1-1h3.5a1 1 0 0 1 1 1c0 1.25.2 2.45.57 3.57a1 1 0 0 1-.25 1z"/></svg>
          555-014-0000
        </li>
        <li>
          <svg viewBox="0 0 24 24" aria-hidden="true"><path fill="var(--gold)" d="M2 5h20v14H2z"/><path fill="none" stroke="var(--card-black)" stroke-width="1.8" d="M2 5l10 8 10-8"/></svg>
          elena@stillwaterreiki.com
        </li>
        <li>
          <svg viewBox="0 0 24 24" aria-hidden="true"><circle cx="12" cy="12" r="10" fill="var(--gold)"/><path fill="none" stroke="var(--card-black)" stroke-width="1.4" d="M2 12h20M12 2c3 3 3 17 0 20M12 2c-3 3-3 17 0 20M4 7h16M4 17h16"/></svg>
          www.stillwaterreiki.com
        </li>
      </ul>
    </div>
  </section>

  <section class="card card--back" aria-label="Business card back">
    <p class="back-mark">STILLWATER REIKI</p>
  </section>

</main>
</body>
</html>
```